Business Card for Ferncliff Massage

I need a business card for my massage therapy & cannabis oil practice. I already have a logo,the "massage" got edited out of this file. I will send the original soon. I need these elements to be on the card:
web: FerncliffMassage.example
ph: 417/283-9061
email: Mirela.Dawkant@mailbox.example
Other slogans, statements to consider:
Science Geek, Massage Therapist, Neuromuscular Therapy, Cannabis Spa Treatments, Raindrop Therapy, Essential Oils
Target Market(s)
women between 20 & 65, people with enough $ to afford regular massage, people who recently had a motor vehicle accident, Halvora HMP insured
Industry/Entity Type
Massage Therapy
Contact Information for Business Card
I would like to see my bear logo featured; contact details, greens & blues preferred colors.

```html
<!DOCTYPE html>
<html lang="en">
<head>
<meta charset="utf-8">
<title>Ferncliff Massage – Business Card</title>
<link rel="stylesheet" href="https://fonts.googleapis.com/css2?family=Tinos&display=swap">
<style>
  :root {
    --page-bg: #d4d4d4;
    --card-white: #ffffff;
    --fern-green: #37803f;
    --fern-green-light: #4b9254;
    --stone-taupe: #a59489;
    --ink: #111111;
  }
  * { box-sizing: border-box; margin: 0; padding: 0; }
  html, body { width: 1189px; height: 1200px; overflow: hidden; }
  body {
    position: relative;
    background: var(--page-bg);
    font-family: "Tinos", "Times New Roman", serif;
  }
  .card {
    position: absolute;
    left: 194px;
    width: 807px;
    height: 460px;
    background: var(--card-white);
    overflow: hidden;
  }
  .card--front { top: 111px; }
  .card--back { top: 619px; }

  .front-band {
    position: absolute;
    left: 0; right: 0; top: 213px; bottom: 0;
    background: linear-gradient(100deg, var(--fern-green) 45%, var(--fern-green-light) 100%);
  }
  .brand-mark {
    position: absolute;
    left: 50%;
    transform: translateX(-50%);
    width: 100px; height: 100px;
    border-radius: 50%;
    background: var(--stone-taupe);
  }
  .card--front .brand-mark { top: 56px; }
  .card--back .brand-mark { top: 110px; }

  .brand-name {
    position: absolute;
    left: 50%;
    transform: translateX(-50%);
    color: var(--fern-green);
    font-weight: 400;
    white-space: nowrap;
    line-height: 1;
  }
  .card--front .brand-name {
    top: 190px;
    font-size: 54px;
    background: var(--card-white);
    padding: 6px 18px 8px;
    border-radius: 16px;
  }
  .card--back .brand-name {
    top: 245px;
    font-size: 66px;
  }

  .contact-list {
    position: absolute;
    left: 64px;
    top: 288px;
    list-style: none;
    color: var(--card-white);
    font-size: 21px;
    line-height: 28.5px;
  }
  .contact-item { display: flex; align-items: center; gap: 16px; white-space: nowrap; }
  .contact-icon {
    width: 18px; height: 18px;
    background: var(--card-white);
    flex: none;
  }
  .contact-icon svg { display: block; width: 18px; height: 18px; }

  .holder-name {
    position: absolute;
    left: 542px;
    top: 322px;
    color: var(--card-white);
    font-size: 30px;
    white-space: nowrap;
  }

  .services {
    position: absolute;
    left: 40px; right: 40px;
    top: 356px;
    text-align: center;
    color: var(--ink);
    font-size: 21px;
    line-height: 26px;
  }
</style>
</head>
<body>

<section class="card card--front">
  <div class="front-band"></div>
  <div class="brand-mark"></div>
  <div class="brand-name">Ferncliff</div>

  <ul class="contact-list">
    <li class="contact-item">
      <span class="contact-icon"><svg viewBox="0 0 18 18"><path d="M5 3h3l1 4-2 1.2c.8 1.8 2 3 3.8 3.8L12 10l4 1v3c0 .6-.4 1-1 1C8.8 15 3 9.2 3 4c0-.6.4-1 1-1z" fill="#37803f"/></svg></span>
      417/283-9061
    </li>
    <li class="contact-item">
      <span class="contact-icon"><svg viewBox="0 0 18 18"><circle cx="9" cy="9" r="6" fill="none" stroke="#37803f" stroke-width="1.6"/><ellipse cx="9" cy="9" rx="2.6" ry="6" fill="none" stroke="#37803f" stroke-width="1.2"/><line x1="3" y1="9" x2="15" y2="9" stroke="#37803f" stroke-width="1.2"/></svg></span>
      FerncliffMassage.example
    </li>
    <li class="contact-item">
      <span class="contact-icon"><svg viewBox="0 0 18 18"><rect x="3" y="5" width="12" height="8" fill="#37803f"/><path d="M3 5l6 5 6-5" fill="none" stroke="#fff" stroke-width="1.2"/></svg></span>
      Mirela.Dawkant@mailbox.example
    </li>
    <li class="contact-item">
      <span class="contact-icon"><svg viewBox="0 0 18 18"><path d="M9 3a4 4 0 0 1 4 4c0 3-4 8-4 8S5 10 5 7a4 4 0 0 1 4-4z" fill="#37803f"/><circle cx="9" cy="7" r="1.5" fill="#fff"/></svg></span>
      2748 NE Alder Crest Ave Portland, OR, 97299
    </li>
  </ul>

  <p class="holder-name">Mirela Dawkant</p>
</section>

<section class="card card--back">
  <div class="brand-mark"></div>
  <div class="brand-name">Ferncliff</div>
  <p class="services">Science Geek, Massage Therapist, Neuromuscular Therapy, Cannabis Spa<br>Treatments, Raindrop Therapy, Essential Oils</p>
</section>

</body>
</html>
```